Yacht, Boats, Watersports company needs a redesign of business card

Hello Designers!
We are a Boat dealership company that sells fun in the water, we sell boats, Yachts, Kayaks and also yacht WaterSport toys. We are looking to redesign our business cards in to something a little bit more sophisticated. in a way that we can make better use of our company colors. I'm attaching a zipped file containing the company 3 sets of company logo which one is an horizontal another one is a vertical and also a chromed 3d logo. Also is included two set of business cards that we use and also some designs that i think it's interesting. We use PMS 2026c Orange and PMS 7687C Blue. I would like to see at least two different options with the orange as accent and also using blue as an accent color. It's really important for the business cards to have a font option and size that is legible to most people. Our current website is wwww.corvellamarine.com. Please visit if you want to have a better feeling of the Boat dealership
You can send Single sided or double side options. We are now using single sided but we may be open for a double side option if we really like the design.
Target Market(s)
Marine, boat sales, yacht sales, water toys sales/
Contact Information for Business Card
Name: Dale Pritchett
Address: 718 West Halden Lane,
Dania Beach, FL 33019
Phone: 954-382-7146
Fax: 954:382-7139
Cell: 954-451-8320
Email: 212@corvellamarine.com
Website: corvellamarine.com
Requirements
Must have
- the current information of the business card provided.
logo
use the PMS Colors
Nice to have
- a touch of elegance and sophistication but simple
Should not have
- should not have any typography that is hard to read, the card should be simple but yet sophisticated.

```html
<!DOCTYPE html>
<html lang="en">
<head>
<meta charset="utf-8">
<title>Corvella Marine – Business Card</title>
<link href="https://fonts.googleapis.com/css2?family=Michroma&family=Roboto:wght@400&display=swap" rel="stylesheet">
<style>
  :root {
    --backdrop: #b8b8b8;
    --navy: #0e467c;
    --orange: #f26532;
    --white: #ffffff;
    --ink: #2b2b2b;
    --shadow: rgba(0,0,0,0.85);
  }
  html, body { margin: 0; padding: 0; overflow: hidden; }
  body { width: 1200px; height: 801px; background: var(--backdrop); position: relative; font-family: 'Roboto', Arial, sans-serif; }
  .card { position: absolute; top: 274px; width: 443px; height: 263px; box-shadow: 2px 2px 1px var(--shadow); overflow: hidden; }
  .card--front { left: 153px; background: var(--white); }
  .card--back { left: 625px; background: var(--navy); }

  .front-band { position: absolute; left: 0; top: 0; width: 323px; height: 70px; background: var(--navy); }
  .front-accent { position: absolute; left: 323px; top: 0; width: 120px; height: 70px; background: var(--orange); }
  .front-seal { position: absolute; left: 266px; top: 6px; width: 112px; height: 112px; border-radius: 50%; background: var(--white); }
  .front-wordmark { position: absolute; left: 26px; top: 30px; font-family: 'Michroma', sans-serif; font-size: 11.5px; letter-spacing: 0.6px; color: var(--white); white-space: nowrap; }

  .holder-name { position: absolute; left: 26px; top: 131px; font-family: 'Michroma', sans-serif; font-size: 13px; letter-spacing: 0.4px; white-space: nowrap; }
  .holder-name .first { color: var(--navy); }
  .holder-name .last { color: var(--orange); margin-left: 6px; }

  .contact-list { position: absolute; left: 26px; top: 161px; margin: 0; padding: 0; list-style: none; }
  .contact-list li { height: 15.6px; line-height: 15.6px; font-size: 12.6px; color: var(--ink); display: flex; align-items: center; white-space: nowrap; }
  .contact-list svg { width: 11px; height: 11px; margin-right: 5px; fill: var(--navy); flex: none; }
  .contact-list .domain { color: var(--navy); }

  .address { position: absolute; right: 26px; top: 208px; text-align: right; font-size: 12.6px; line-height: 15.6px; color: var(--ink); }

  .back-seal { position: absolute; left: 187px; top: 81px; width: 70px; height: 70px; border-radius: 50%; background: var(--white); }
  .back-wordmark { position: absolute; left: 0; right: 0; top: 164px; text-align: center; font-family: 'Michroma', sans-serif; font-size: 16px; letter-spacing: 1px; color: var(--white); white-space: nowrap; }
</style>
</head>
<body>
  <section class="card card--front">
    <div class="front-band"></div>
    <div class="front-accent"></div>
    <div class="front-seal"></div>
    <div class="front-wordmark">CORVELLA MARINE</div>

    <div class="holder-name"><span class="first">DALE</span><span class="last">PRITCHETT</span></div>

    <ul class="contact-list">
      <li><svg viewBox="0 0 24 24"><path d="M6.6 10.8c1.4 2.8 3.8 5.1 6.6 6.6l2.2-2.2c.3-.3.7-.4 1-.2 1.1.4 2.3.6 3.6.6.6 0 1 .4 1 1V20c0 .6-.4 1-1 1C10.6 21 3 13.4 3 4c0-.6.4-1 1-1h3.5c.6 0 1 .4 1 1 0 1.3.2 2.5.6 3.6.1.3 0 .7-.2 1z"/></svg>954-382-7146</li>
      <li><svg viewBox="0 0 24 24"><path d="M6 2h12v5H6zM4 8h16a2 2 0 0 1 2 2v7h-4v5H6v-5H2v-7a2 2 0 0 1 2-2zm4 8v4h8v-4z"/></svg>954:382-7139</li>
      <li><svg viewBox="0 0 24 24"><path d="M7 1h10a2 2 0 0 1 2 2v18a2 2 0 0 1-2 2H7a2 2 0 0 1-2-2V3a2 2 0 0 1 2-2zm0 3v14h10V4zm5 15.5a1 1 0 1 0 0 2 1 1 0 0 0 0-2z"/></svg>954-451-8320</li>
      <li><svg viewBox="0 0 24 24"><path d="M2 5h20v14H2zm2 2v.5l8 5.5 8-5.5V7z"/></svg>212@corvellamarine.com</li>
      <li><svg viewBox="0 0 24 24"><path d="M12 2a10 10 0 1 0 0 20 10 10 0 0 0 0-20zm-1 2.1V8H7.3A8 8 0 0 1 11 4.1zM13 4.1A8 8 0 0 1 16.7 8H13zM4.6 10H11v4H4.6a8 8 0 0 1 0-4zM13 10h6.4a8 8 0 0 1 0 4H13zM7.3 16H11v3.9A8 8 0 0 1 7.3 16zM13 16h3.7a8 8 0 0 1-3.7 3.9z"/></svg>www.<span class="domain">corvellamarine</span>.com</li>
    </ul>

    <address class="address" style="font-style:normal">718 West Halden Lane<br>Dania Beach, FL 33019</address>
  </section>

  <section class="card card--back">
    <div class="back-seal"></div>
    <div class="back-wordmark">CORVELLA MARINE</div>
  </section>
</body>
</html>
```